Redesign web application

we are a Vitalink start up. we need a new design for our platform that allows users, their family and docs to access their detailed stats online
users take readings using our wireless devices that transmit the readings to our server in the background All this happens in real time . and users can instantly login to the portal to view readings , make comments, , view charts,
if readings are not within in prescribed thresholds then alerts are reported on the website, SMS and email
please see the screenshots of existing pages
We need the following pages re designed
login page
patient DB summary , patient DB condition
Doc DB
Nurse DB
After you submit designs and we choose the winning design . please help to make minor modifications after that so that we can use it
Target Market(s)
Paying
Doctors/ Clinics/Clinic chains/ Specialists will be the ones who are paying for the service. the service
Non Paying
patients family members, doctors all will be accessing the system to view readings, alerts , make comments , see charts
Industry/Entity Type
Health
Colors
Designer to choose colors to be used in the design.
Look and feel

```html
<!DOCTYPE html>
<html lang="en">
<head>
<meta charset="utf-8">
<title>Vitalink – Welcome</title>
<link href="https://fonts.googleapis.com/css2?family=Open+Sans:wght@400;600;700&family=Arimo:wght@400&display=swap" rel="stylesheet">
<style>
:root{
  --green:#7aab1e;
  --green-dark:#5f8c12;
  --blue:#2e8fe0;
  --text:#666;
  --text-dark:#444;
  --muted:#999;
  --band:#efefef;
  --white:#fff;
  --pill:#f1f1f1;
  --footer-box:#1b1c1c;
  --footer-field:#2c2d2d;
  --footer-link:#9a9a9a;
}
*{box-sizing:border-box;margin:0;padding:0}
html,body{width:1200px;height:1000px;overflow:hidden}
body{position:relative;font-family:"Open Sans",Arial,sans-serif;color:var(--text);background:var(--white)}
.abs{position:absolute}
.band-top{left:0;top:0;width:1200px;height:292px;background:var(--band)}
.band-bottom{left:0;top:704px;width:1200px;height:296px;background:var(--band)}

.brand{display:flex;align-items:center;gap:6px;font-weight:600;color:var(--green)}
.brand-dot{border-radius:50%;background:var(--green)}
.brand-top{left:289px;top:31px;font-size:32px}
.brand-top .brand-dot{width:42px;height:42px}

.welcome-title{left:289px;top:118px;font-size:17px;color:var(--text);letter-spacing:.3px}
.rule{height:1px;background:#dcdcdc}
.rule-accent{height:3px;background:var(--green)}
.intro-lead{left:289px;top:180px;font-size:13px;color:var(--text)}
.intro-lead b{color:var(--text-dark)}
.intro-body{left:289px;top:208px;width:425px;font-size:9.6px;line-height:12.5px;color:#888}
.intro-body span{color:var(--green)}

.login-card{left:763px;top:41px;width:203px;height:214px;background:var(--white);border-radius:3px;box-shadow:0 8px 6px -6px rgba(0,0,0,.25)}
.login-tab{left:776px;top:62px;width:64px;height:27px;background:var(--blue);color:#fff;font-size:12px;padding:6px 0 0 14px;border-radius:2px 2px 0 0}
.login-line{left:776px;top:87px;width:180px;height:3px;background:var(--blue)}
.field{left:777px;width:178px;height:31px;border:2px solid #e2e2e2;border-radius:3px;background:#faf9f9;font-size:9.5px;color:#777;display:flex;align-items:center;padding-left:11px;gap:5px}
.btn-green{background:linear-gradient(#94c52a,var(--green-dark));color:#fff;font-weight:700;border-radius:3px;display:flex;align-items:center;justify-content:center;font-size:10.5px}
.sign-in{left:777px;top:175px;width:64px;height:28px}
.login-links{left:777px;top:222px;font-size:8px;color:#777}

.section-title{display:flex;align-items:center;gap:9px;font-size:13.5px;color:var(--text);letter-spacing:.3px}
.news-img{left:289px;top:385px;width:210px;height:107px;background:linear-gradient(#f6f4e6 0%,#ebe9d4 55%,#9aa57a 75%,#6d7a4c 100%)}
.news-title{left:289px;top:504px;font-size:11px;color:var(--text-dark)}
.news-meta{left:289px;top:521px;font-size:8px;color:var(--muted)}
.news-body{left:289px;top:538px;width:210px;font-size:9px;line-height:12.5px;color:#888}
.view-all{left:289px;top:591px;width:71px;height:23px}

.service{left:523px;width:209px;height:24px;border-radius:12px;background:var(--pill);font-size:9px;color:var(--text);display:flex;align-items:center;padding-left:36px}
.service.open{background:#e8e8e8}
.service .dot{position:absolute;left:0;top:-1px;width:26px;height:26px;border-radius:50%;background:var(--green);color:#fff;font-size:9px;display:flex;align-items:center;justify-content:center}
.service.open .dot{background:var(--blue)}
.service-body{left:559px;top:447px;width:166px;font-size:9px;line-height:12.5px;color:#888}

.video-frame{left:756px;top:385px;width:211px;height:119px;background:#000}
.video-still{left:764px;top:392px;width:195px;height:94px;background:linear-gradient(90deg,#9c6a3c,#c79a60 40%,#d6d3cc 75%,#8f8f8f)}
.video-bar{left:791px;top:491px;width:128px;height:5px;border:1px solid #555;border-radius:2px}
.video-caption{left:756px;top:515px;font-size:9px;color:var(--green)}
.video-sub{left:757px;top:541px;font-size:9.5px;font-weight:700;color:var(--text-dark)}
.video-list{left:757px;top:559px;list-style:none;font-size:9px;color:var(--text)}
.video-list li{height:14.3px;display:flex;align-items:center;gap:6px}
.video-list li::before{content:"";border-left:6px solid #bbb;border-top:4px solid transparent;border-bottom:4px solid transparent}
.video-list li.active{color:var(--blue)}
.video-list li.active::before{border-left-color:var(--blue)}
.video-all{left:756px;top:631px;font-size:9.5px;color:var(--text-dark)}

.address{left:289px;font-size:9.5px;line-height:13.6px;color:var(--text-dark)}
.footer-box{left:522px;top:748px;width:444px;height:215px;background:var(--footer-box)}
.brand-foot{left:548px;top:784px;font-size:21px}
.brand-foot .brand-dot{width:28px;height:28px}
.foot-links{font-family:Arimo,Arial,sans-serif;list-style:none;font-size:8.3px;color:var(--footer-link)}
.foot-links li{height:16.3px}
.subscribe{left:551px;top:846px;font-family:Arimo,Arial,sans-serif;font-size:9px;color:#8a8a8a}
.email{left:551px;top:864px;width:181px;height:31px;background:var(--footer-field);border-radius:2px;display:flex;align-items:center;padding-left:13px;gap:6px;font-family:Arimo,Arial,sans-serif;font-size:8.5px;color:#8a8a8a}
.email-split{left:698px;top:868px;width:1px;height:23px;background:#111}
.email-go{left:713px;top:872px;color:#aaa;font-size:10px}
.foot-rule{left:552px;top:925px;width:392px;height:1px;background:#2e2f2f}
.copyright{left:552px;top:936px;font-family:Arimo,Arial,sans-serif;font-size:8px;color:#8a8a8a}
</style>
</head>
<body>
<div class="abs band-top"></div>
<div class="abs band-bottom"></div>

<!-- Header -->
<div class="abs brand brand-top"><span class="brand-dot"></span>Vitalink</div>
<h1 class="abs welcome-title" style="font-weight:400">WELCOME YOU !</h1>
<div class="abs rule" style="left:289px;top:148px;width:423px"></div>
<div class="abs rule-accent" style="left:289px;top:147px;width:50px"></div>
<p class="abs intro-lead"><b>Lorem Ipsum</b> is simply dummy text of the printing</p>
<p class="abs intro-body">Lorem Ipsum is simply dummy text of the printing and typesetting industry. Lorem Ipsum has been the industry's standard dummy <span>text ever since the 1500s, when</span> an unknown printer took a galley of type and scrambled it to make a type specimen book. It has survived not only five centuries, but also the leap into electronic typesetting</p>

<!-- Login -->
<div class="abs login-card"></div>
<div class="abs login-tab">Login</div>
<div class="abs login-line"></div>
<div class="abs field" style="top:99px">
  <svg width="10" height="11" viewBox="0 0 10 11"><circle cx="5" cy="3" r="2.6" fill="#333"/><path d="M0 11c0-3.5 2.2-5 5-5s5 1.5 5 5z" fill="#333"/></svg>Login ID</div>
<div class="abs field" style="top:135px">
  <svg width="10" height="11" viewBox="0 0 10 11"><path d="M2.5 5V3.5a2.5 2.5 0 0 1 5 0V5" stroke="#333" stroke-width="1.4" fill="none"/><rect x="1" y="5" width="8" height="6" rx="1" fill="#333"/></svg>Password</div>
<div class="abs btn-green sign-in">Sign In</div>
<p class="abs login-links">Password Forgotten ? &nbsp;|&nbsp; New User</p>

<!-- Latest news -->
<h2 class="abs section-title" style="left:289px;top:345px;font-weight:400">
  <svg width="14" height="13" viewBox="0 0 14 13"><rect x=".5" y=".5" width="13" height="12" fill="none" stroke="#aaa"/><rect x="2.5" y="2.5" width="4" height="4" fill="#bbb"/><path d="M8 3h4M8 5.5h4M2.5 8.5h9.5M2.5 10.5h9.5" stroke="#bbb"/></svg>LATEST NEWS</h2>
<div class="abs rule" style="left:289px;top:369px;width:209px"></div>
<div class="abs rule-accent" style="left:289px;top:368px;width:42px"></div>
<div class="abs news-img" role="img" aria-label="Photo of a woman jogging in a park with a city skyline behind"></div>
<h3 class="abs news-title" style="font-weight:400">Lorem Ipsum is simply dummy</h3>
<p class="abs news-meta">25 June 2014 &nbsp;|&nbsp; 4 Comments</p>
<p class="abs news-body">Lorem Ipsum is simply dummy text of the printing and typesetting industry. Lorem Ipsum has been the industry's standard dummy</p>
<div class="abs btn-green view-all" style="font-weight:600">View All &nbsp;›</div>

<!-- Services -->
<h2 class="abs section-title" style="left:522px;top:345px;font-weight:400">
  <svg width="19" height="15" viewBox="0 0 19 15"><circle cx="13" cy="6" r="4.5" fill="none" stroke="#aaa" stroke-width="2.4" stroke-dasharray="2 1.2"/><circle cx="5" cy="11" r="3.2" fill="none" stroke="#bbb" stroke-width="2" stroke-dasharray="1.6 1"/></svg>OUR SERVICES</h2>
<div class="abs rule" style="left:522px;top:369px;width:210px"></div>
<div class="abs rule-accent" style="left:522px;top:368px;width:42px"></div>
<div class="abs service" style="top:386px"><span class="dot">+</span>Lorem Ipsum is simply dummy printing</div>
<div class="abs service open" style="top:413px"><span class="dot">-</span>Lorem Ipsum is simply dummy printing</div>
<p class="abs service-body">Lorem Ipsum is simply dummy text of the printing and typesetting industry. Lorem Ipsum has been the industry's standard dummy text ever since</p>
<div class="abs service" style="top:515px"><span class="dot">+</span>Lorem Ipsum is simply dummy printing</div>
<div class="abs service" style="top:542px"><span class="dot">+</span>Lorem Ipsum is simply dummy printing</div>

<!-- Videos -->
<h2 class="abs section-title" style="left:756px;top:345px;font-weight:400">
  <svg width="13" height="12" viewBox="0 0 13 12"><rect x=".5" y=".5" width="12" height="11" fill="none" stroke="#aaa"/><path d="M3 .5v11M10 .5v11M.5 6h12" stroke="#aaa"/></svg>VIDEOS</h2>
<div class="abs rule" style="left:756px;top:369px;width:210px"></div>
<div class="abs rule-accent" style="left:756px;top:368px;width:42px"></div>
<div class="abs video-frame"></div>
<div class="abs video-still" role="img" aria-label="Video still of green apples in a bowl beside a dumbbell and measuring tape"></div>
<svg class="abs" style="left:768px;top:488px" width="9" height="10" viewBox="0 0 9 10"><path d="M1 1l7 4-7 4z" fill="#ddd"/></svg>
<div class="abs video-bar"></div>
<p class="abs video-caption">Lorem Ipsum is simply dummy text of the printing</p>
<h3 class="abs video-sub">Watch other Videos</h3>
<ul class="abs video-list">
  <li>Lorem Ipsum is simply dummy</li>
  <li class="active">was popularised in the 1960</li>
  <li>leap into electronic typesetting</li>
  <li>unknown printer took a galley of type &amp; scrambled</li>
</ul>
<p class="abs video-all">View All &nbsp;›</p>

<!-- Locations -->
<h2 class="abs section-title" style="left:289px;top:747px;font-weight:400">
  <svg width="9" height="13" viewBox="0 0 9 13"><path d="M4.5 13S0 7.5 0 4.5a4.5 4.5 0 0 1 9 0C9 7.5 4.5 13 4.5 13z" fill="#aaa"/><circle cx="4.5" cy="4.5" r="1.7" fill="#efefef"/></svg>OUR LOCATIONS</h2>
<div class="abs rule" style="left:289px;top:770px;width:208px"></div>
<div class="abs rule-accent" style="left:289px;top:769px;width:42px"></div>
<address class="abs address" style="top:783px;font-style:normal">#123, Street Name, Location<br>Lorem Ipsum<br>City Name, Country- 1234<br>Call: <b>123 456 78900</b></address>
<address class="abs address" style="top:853px;font-style:normal">#123, Street Name, Location<br>Lorem Ipsum<br>City Name, Country- 1234<br>Call: <b>123 456 78900</b></address>

<!-- Footer -->
<div class="abs footer-box"></div>
<div class="abs brand brand-foot"><span class="brand-dot"></span>Vitalink</div>
<ul class="abs foot-links" style="left:756px;top:785px">
  <li>About Us</li><li>Careers</li><li>News</li><li>Patient DB SUmmary</li><li>Patient DB Condition</li><li>DOC DB</li><li>Nurse DB</li>
</ul>
<ul class="abs foot-links" style="left:866px;top:785px">
  <li>About Us</li><li>Careers</li><li>News</li><li>Patient DB SUmmary</li><li>Patient DB Condition</li><li>DOC DB</li><li>Nurse DB</li>
</ul>
<p class="abs subscribe">Subscribe and alert in your inbox</p>
<div class="abs email">
  <svg width="11" height="8" viewBox="0 0 11 8"><rect width="11" height="8" fill="#777"/><path d="M0 0l5.5 4.5L11 0" stroke="#2c2d2d" fill="none"/></svg>Enter Your Email</div>
<div class="abs email-split"></div>
<span class="abs email-go">❯</span>
<div class="abs foot-rule"></div>
<p class="abs copyright">All Right Reserved 2014 | Privacy Policy</p>
</body>
</html>
```